Automotive eCommerce Business looking for a business card design

Looking for a clean and simple business card design. Our company name is "Tundra Motors" and we are a company specializing in the ecommerce sales of automotive parts, specifically for pick up trucks and large SUVs. Our company colours are red, black, and white.

Feel free to use the logo provided or create a new logo that you seem fit. Looking forward to your creative ideas!

Industry/Entity Type

Automotive

Contact Information for Business Card

We were thinking of a possibly two-sided design featuring just the logo and company name on one side, and personal information on the other side. Single sided designs will be considered as well.

Font styles to use
Serif
Sans Serif
Decorative

Colors
ec1f27
ffffff
000000

Requirements
Must have
• Space for employee's name, title, phone number and email address, along with the company address and website somewhere.

```html
<!DOCTYPE html>
<html lang="en">
<head>
<meta charset="utf-8">
<title>Tundra Motors Ltd — Business Card</title>
<link href="https://fonts.googleapis.com/css2?family=Jost:wght@400;500&family=Work+Sans:wght@400;500&display=swap" rel="stylesheet">
<style>
  :root {
    --brand-red: #ec1f27;
    --ink: #000000;
    --paper: #ffffff;
    --backdrop: #3a3a3a;
    --muted: #222222;
  }
  * { box-sizing: border-box; margin: 0; padding: 0; }
  html, body { width: 1200px; height: 900px; overflow: hidden; }
  body {
    background: var(--backdrop);
    display: flex;
    flex-direction: column;
    align-items: center;
    justify-content: center;
    gap: 44px;
  }
  .card {
    position: relative;
    width: 580px;
    height: 331px;
    box-shadow: 0 8px 24px rgba(0,0,0,0.35);
    overflow: hidden;
  }

  /* Front side */
  .card--front {
    background: var(--brand-red);
    display: flex;
    flex-direction: column;
    align-items: center;
    justify-content: center;
    gap: 18px;
  }
  .brand-dot {
    width: 74px;
    height: 74px;
    border-radius: 50%;
    background: var(--ink);
  }
  .brand-name {
    font-family: "Jost", sans-serif;
    font-weight: 500;
    font-size: 27px;
    letter-spacing: 1px;
  }
  .card--front .brand-name { color: var(--ink); }

  /* Back side */
  .card--back { background: var(--paper); }
  .edge-bar {
    position: absolute;
    left: 0;
    top: 62px;
    width: 9px;
    height: 118px;
    background: var(--ink);
  }
  .person {
    position: absolute;
    left: 34px;
    top: 58px;
  }
  .person__name {
    font-family: "Jost", sans-serif;
    font-weight: 500;
    font-size: 24px;
    letter-spacing: 1px;
    color: var(--brand-red);
    text-transform: uppercase;
    line-height: 1;
  }
  .person__title {
    font-family: "Work Sans", sans-serif;
    font-size: 15px;
    color: var(--muted);
    margin-top: 6px;
  }
  .divider {
    position: absolute;
    left: 120px;
    right: 50px;
    top: 228px;
    height: 2px;
    background: var(--ink);
  }
  .contacts {
    position: absolute;
    left: 34px;
    top: 126px;
    list-style: none;
    font-family: "Work Sans", sans-serif;
    font-size: 15px;
    color: var(--muted);
  }
  .contacts li {
    display: flex;
    align-items: center;
    gap: 9px;
    height: 22px;
  }
  .contacts svg { width: 11px; height: 11px; flex: none; }
  .contacts .accent { color: var(--brand-red); }
  .back-brand {
    position: absolute;
    right: 50px;
    top: 98px;
    display: flex;
    flex-direction: column;
    align-items: center;
    gap: 12px;
  }
  .back-brand .brand-dot {
    width: 62px;
    height: 62px;
    background: var(--brand-red);
  }
  .back-brand .brand-name {
    font-size: 25px;
    color: var(--ink);
  }
</style>
</head>
<body>

  <section class="card card--front" aria-label="Card front">
    <div class="brand-dot"></div>
    <p class="brand-name">Tundra Motors Ltd</p>
  </section>

  <section class="card card--back" aria-label="Card back">
    <div class="edge-bar"></div>

    <div class="person">
      <p class="person__name">Mason Keller</p>
      <p class="person__title">Director</p>
    </div>

    <ul class="contacts">
      <li>
        <svg viewBox="0 0 12 12" aria-hidden="true"><path d="M2.5 1 L4.5 1 L5 3.5 L3.8 4.4 Q5 7 7.6 8.2 L8.5 7 L11 7.5 L11 9.5 Q10.5 11 9 11 Q1 10 1 2.5 Q1 1 2.5 1Z" fill="var(--brand-red)"/></svg>
        <span>555.201.4418</span>
      </li>
      <li>
        <svg viewBox="0 0 12 12" aria-hidden="true"><rect x="3" y="0.8" width="6" height="10.4" rx="1" fill="none" stroke="var(--brand-red)" stroke-width="1.4"/><circle cx="6" cy="9" r="0.8" fill="var(--brand-red)"/></svg>
        <span>555.347.9062</span>
      </li>
      <li>
        <svg viewBox="0 0 12 12" aria-hidden="true"><rect x="0.8" y="2.2" width="10.4" height="7.6" fill="none" stroke="var(--brand-red)" stroke-width="1.3"/><path d="M1 2.6 L6 6.6 L11 2.6" fill="none" stroke="var(--brand-red)" stroke-width="1.3"/></svg>
        <span>info@tundramotorsltd.com</span>
      </li>
      <li>
        <svg viewBox="0 0 12 12" aria-hidden="true"><circle cx="6" cy="6" r="5" fill="none" stroke="var(--brand-red)" stroke-width="1.2"/><ellipse cx="6" cy="6" rx="2.2" ry="5" fill="none" stroke="var(--brand-red)" stroke-width="1"/><path d="M1 6 H11" stroke="var(--brand-red)" stroke-width="1"/></svg>
        <span>www.<span class="accent">tundramotorsltd</span>.com</span>
      </li>
    </ul>

    <div class="back-brand">
      <div class="brand-dot"></div>
      <p class="brand-name">Tundra Motors Ltd</p>
    </div>

    <div class="divider"></div>
  </section>

</body>
</html>
```